Building and constructions

Extension, additions, alterations, renovations, new homes, project management and supervision

Industry/Entity Type

Building

Contact Information for Business Card

Tolvane building service constructions PTY LTD
Marcus Delveno builder/ supervisor
BLD 71940 member of RHG
0412735190 email tmrk41@qelmora.com

```html
<!DOCTYPE html>
<html lang="en">
<head>
<meta charset="utf-8">
<title>Tolvane Building Service – Business Card</title>
<link href="https://fonts.googleapis.com/css2?family=Montserrat:wght@300;400;600;700&display=swap" rel="stylesheet">
<style>
  :root {
    --bg: #e9e6e1;
    --card-white: #fbfbfb;
    --blue: #1b8fd0;
    --blue-deep: #0f6fb3;
    --blue-light: #2aa7e0;
    --green: #8dc63f;
    --grey-text: #8a8a8a;
    --dark-text: #4a4a4a;
    --photo-a: #5d6670;
    --photo-b: #a9c6d6;
  }
  * { margin: 0; padding: 0; box-sizing: border-box; }
  html, body {
    width: 1200px; height: 780px; overflow: hidden;
    background: var(--bg);
    font-family: "Montserrat", sans-serif;
  }
  .stage {
    width: 1200px; height: 780px;
    display: flex; align-items: center; justify-content: center; gap: 20px;
  }
  .card {
    position: relative;
    width: 570px; height: 326px;
    border-radius: 16px;
    overflow: hidden;
    box-shadow: 0 6px 18px rgba(0,0,0,.18);
  }
  .card-front { background: var(--card-white); }
  .card-shapes { position: absolute; inset: 0; }

  .brand {
    position: absolute; left: 34px; top: 92px;
    display: flex; align-items: center; gap: 10px;
  }
  .brand-mark { width: 22px; height: 22px; background: var(--blue); }
  .brand-name {
    font-weight: 700; font-size: 21px; color: var(--blue);
    letter-spacing: .5px; text-transform: uppercase; line-height: 1.05;
  }
  .brand-sub {
    position: absolute; left: 66px; top: 142px;
    font-size: 8.5px; letter-spacing: 4px; color: var(--grey-text);
    text-transform: uppercase;
  }
  .person { position: absolute; left: 34px; top: 182px; }
  .person-name {
    font-weight: 700; font-size: 22px; color: var(--blue);
    text-transform: uppercase; letter-spacing: .3px;
  }
  .person-role { font-size: 15px; color: var(--dark-text); font-weight: 300; }

  .services {
    position: absolute; right: 28px; top: 24px;
    list-style: none; text-align: right;
  }
  .services li {
    font-size: 13px; color: var(--grey-text); font-weight: 300;
    line-height: 18px;
    display: flex; align-items: center; justify-content: flex-end; gap: 10px;
  }
  .services li::after {
    content: ""; width: 7px; height: 7px; border-radius: 50%;
    background: var(--green);
  }
  .contact {
    position: absolute; right: 28px; top: 168px;
    list-style: none; text-align: right;
  }
  .contact li {
    font-size: 14px; color: var(--dark-text); line-height: 22px;
    display: flex; align-items: center; justify-content: flex-end; gap: 8px;
  }
  .contact-icon {
    width: 15px; height: 15px; background: var(--blue); border-radius: 3px;
    display: inline-flex; align-items: center; justify-content: center;
  }
  .licence {
    position: absolute; right: 30px; bottom: 22px;
    color: #fff; font-size: 14px; letter-spacing: .3px;
  }

  .card-back { background: linear-gradient(160deg, var(--blue-light), var(--blue-deep)); }
  .back-title {
    position: absolute; left: 0; right: 0; top: 112px;
    text-align: center; color: #fff;
  }
  .back-name {
    font-weight: 700; font-size: 26px; text-transform: uppercase; letter-spacing: .5px;
    text-shadow: 0 1px 3px rgba(0,0,0,.35);
  }
  .back-sub {
    font-size: 15px; letter-spacing: 6px; text-transform: uppercase; margin-top: 2px;
    font-weight: 300; text-shadow: 0 1px 3px rgba(0,0,0,.35);
  }
  .back-tag {
    font-size: 12px; letter-spacing: 7px; margin-top: 8px;
    text-shadow: 0 1px 3px rgba(0,0,0,.35);
  }
</style>
</head>
<body>
<main class="stage">

  <section class="card card-front" aria-label="Business card front">
    <svg class="card-shapes" viewBox="0 0 570 326" preserveAspectRatio="none" aria-hidden="true">
      <defs>
        <linearGradient id="band-blue" x1="0" y1="0" x2="1" y2="1">
          <stop offset="0" stop-color="#2aa7e0"/>
          <stop offset="1" stop-color="#0f6fb3"/>
        </linearGradient>
      </defs>
      <path d="M40,326 C230,305 430,255 570,148 L570,168 C430,268 250,318 90,326 Z" fill="#8dc63f"/>
      <path d="M110,326 C290,312 450,262 570,178 L570,326 Z" fill="url(#band-blue)"/>
    </svg>

    <div class="brand">
      <span class="brand-mark"></span>
      <span class="brand-name">Tolvane Building Service</span>
    </div>
    <div class="brand-sub">Constructions PTY LTD</div>

    <div class="person">
      <div class="person-name">Marcus Delveno</div>
      <div class="person-role">builder/ supervisor</div>
    </div>

    <ul class="services">
      <li>Extension</li>
      <li>Additions</li>
      <li>Alterations</li>
      <li>Renovations</li>
      <li>New homes</li>
      <li>Project management</li>
      <li>Supervision</li>
    </ul>

    <ul class="contact">
      <li>0412735190
        <span class="contact-icon">
          <svg width="10" height="10" viewBox="0 0 24 24" aria-hidden="true"><path fill="#fff" d="M6.6 10.8a15 15 0 0 0 6.6 6.6l2.2-2.2c.3-.3.7-.4 1-.2 1.1.4 2.3.6 3.6.6.6 0 1 .4 1 1V20c0 .6-.4 1-1 1C10.6 21 3 13.4 3 4c0-.6.4-1 1-1h3.5c.6 0 1 .4 1 1 0 1.3.2 2.5.6 3.6.1.3 0 .7-.2 1z"/></svg>
        </span>
      </li>
      <li>tmrk41@qelmora.com
        <span class="contact-icon">
          <svg width="10" height="10" viewBox="0 0 24 24" aria-hidden="true"><path fill="none" stroke="#fff" stroke-width="2.4" d="M3 6h18v12H3zM3 6l9 7 9-7"/></svg>
        </span>
      </li>
    </ul>

    <div class="licence">BLD 71940 member of RHG</div>
  </section>

  <section class="card card-back" aria-label="Business card back">
    <svg class="card-shapes" viewBox="0 0 570 326" preserveAspectRatio="none">
      <defs>
        <linearGradient id="photo-tone" x1="0" y1="0" x2="1" y2="1">
          <stop offset="0" stop-color="#a9c6d6"/>
          <stop offset="1" stop-color="#5d6670"/>
        </linearGradient>
      </defs>
      <polygon points="0,70 0,150 400,326 490,326" fill="#ffffff"/>
      <polygon points="0,92 0,140 420,326 470,326" fill="#8dc63f"/>
      <polygon points="70,0 180,0 570,180 570,250" fill="#ffffff"/>
      <polygon points="110,0 160,0 570,200 570,232" fill="#8dc63f"/>
      <polygon points="0,0 100,0 570,215 570,326 445,326 0,120" fill="url(#photo-tone)" role="img" aria-label="Photo of a finished home exterior with pool"/>
    </svg>
    <div class="back-title">
      <div class="back-name">Tolvane Building Service</div>
      <div class="back-sub">Constructions PTY LTD</div>
      <div class="back-tag">commercial &amp; residential</div>
    </div>
  </section>

</main>
</body>
</html>
```